Medical Practice Brochure Design Project

We are a medical practice in Denver, Colorado and we need to design a brochure to promote one subset of services we offer. We perform Bureau of Freight Haulage (BFH) physical exams and also perform BFH drug testing onsite and want a brochure that outlines these services. This brochure will be used a part of a marketing package to promote this service to businesses that employ individuals that drive commercial vehicles.

Project Deadline Extended Reason: I am going extend the deadline for submissions. Ending on a Sunday is going to limit last minute submissions. As a trade off, I am going to guarantee this project. Thanks for all the submissions. Added Thursday, October 09, 2014

Target Market(s)

human resource managers, companies that deploy commercial vehicles (i.e. trucks and tractor trailers), independent drivers / contractors

Industry/Entity Type

Medical

Font styles to use
Sans Serif

Colors
0455a3

Requirements
Must have
• Our logo, our web address (kellanmoorclinic.com), our phone number and fax number, professional look and feel, layout be a trifold 8.5x11 (see templates), map to our location (see attached for example).
Nice to have
• Our logo (birchwell family medicine) should not be the focus of the brochure. Text items that should stand out should be "BFH Examination", "BFH Drug Testing" and "QWLPA Certified Providers", our phone number, and our web address. We also will have the ability to have clients schedule appointment online through our website which should be indicated in the brochure in a prominent manner.
Should not have
• no images of crosses, no images of syringes

```html
<!DOCTYPE html>
<html lang="en">
<head>
<meta charset="utf-8">
<title>Birchwell Family Medicine – BFH Trifold Brochure</title>
<link rel="stylesheet" href="https://fonts.googleapis.com/css2?family=Montserrat:wght@300;400;600;700&display=swap">
<style>
  :root {
    --brand-blue: #0455a3;
    --deep-navy: #1c3f78;
    --mid-blue: #2f73c4;
    --sky-blue: #5a9be0;
    --pale-grey: #f1f2f4;
    --stage: #e9e9ea;
    --ink-light: #ffffff;
    --ink-dark: #2b2f36;
    --map-grey: #c9cbcf;
    --font-main: "Montserrat", Arial, sans-serif;
  }
  * { box-sizing: border-box; margin: 0; padding: 0; }
  html, body { width: 840px; height: 1200px; overflow: hidden; }
  body { background: var(--stage); font-family: var(--font-main); color: var(--ink-dark); position: relative; }

  .spread {
    position: absolute; left: 90px; width: 660px; height: 500px;
    display: flex; box-shadow: 0 12px 28px rgba(0,0,0,.18);
  }
  .spread--outside { top: 40px; }
  .spread--inside { top: 650px; }
  .panel { position: relative; width: 220px; height: 100%; overflow: hidden; }
  .panel + .panel { border-left: 1px solid rgba(0,0,0,.06); }

  /* ---------- outside: back panel ---------- */
  .panel--cover-back { background: var(--deep-navy); color: var(--ink-light); }
  .cover-back__photo {
    position: absolute; left: 0; right: 0; bottom: 0; height: 260px;
    background: linear-gradient(180deg, rgba(28,63,120,0) 0%, #2a4f8a 40%, #173463 100%);
  }
  .cover-back__title {
    position: absolute; top: 70px; left: 22px; right: 18px;
    font-weight: 300; font-size: 19px; line-height: 1.2;
  }
  .cover-back__text {
    position: absolute; top: 158px; left: 22px; right: 22px;
    font-size: 9.5px; line-height: 1.45; font-weight: 400;
  }

  /* ---------- outside: contact panel ---------- */
  .panel--contact { background: var(--pale-grey); }
  .contact__heading {
    position: absolute; top: 24px; left: 18px;
    font-weight: 300; font-size: 18px; color: var(--brand-blue); letter-spacing: .5px;
  }
  .contact__address {
    position: absolute; top: 52px; left: 18px;
    font-size: 8px; font-weight: 700; color: var(--brand-blue); line-height: 1.4; text-transform: uppercase;
  }
  .contact__map {
    position: absolute; top: 88px; left: 14px; width: 192px; height: 118px;
    background: linear-gradient(135deg, #ffffff 0%, #e3e5e8 100%);
    border-radius: 2px;
  }
  .contact__directions {
    position: absolute; top: 214px; left: 18px; right: 18px;
    font-size: 6.5px; line-height: 1.45; color: #555a62;
  }
  .contact__wave { position: absolute; left: 0; bottom: 0; width: 220px; height: 240px; }
  .contact__details {
    position: absolute; left: 0; right: 0; top: 300px; text-align: center; color: var(--ink-light);
  }
  .brand-name {
    display: inline-flex; align-items: center; gap: 6px;
    font-weight: 700; font-size: 12px; letter-spacing: .4px; text-transform: uppercase;
  }
  .brand-name__dot { width: 9px; height: 9px; border-radius: 50%; background: currentColor; }
  .contact__phone { margin-top: 14px; font-size: 12px; font-weight: 600; line-height: 1.5; }
  .web-address {
    position: absolute; left: 0; right: 0; bottom: 22px; text-align: center;
    font-size: 11px; font-weight: 700; color: var(--brand-blue);
  }

  /* ---------- outside: front cover ---------- */
  .panel--cover-front { background: #ffffff; }
  .cover-front__brand {
    position: absolute; top: 20px; left: 0; right: 0; text-align: center; color: var(--brand-blue);
  }
  .cover-front__photo {
    position: absolute; top: 58px; left: 0; right: 0; height: 170px;
    background: linear-gradient(160deg, #b7bcc4 0%, #7e8a99 55%, #4d5a6b 100%);
  }
  .cover-front__band { position: absolute; left: 0; top: 200px; width: 220px; height: 300px; }
  .cover-front__services {
    position: absolute; top: 262px; left: 0; right: 0; text-align: center;
    color: var(--ink-light); font-weight: 600; font-size: 12.5px; line-height: 1.35; text-transform: uppercase;
  }
  .cover-front__services li { list-style: none; margin-bottom: 12px; }

  /* ---------- inside ---------- */
  .spread--inside .panel { background: var(--mid-blue); }
  .inside__photo { position: absolute; top: 0; left: 0; right: 0; height: 210px; }
  .inside__photo--eye { background: linear-gradient(135deg, #f4f6f8 0%, #c6ccd4 60%, #8b97a6 100%); }
  .inside__photo--pressure { background: linear-gradient(160deg, #e2e5e9 0%, #9aa3ad 50%, #5a4a40 100%); }
  .inside__photo--ear { background: linear-gradient(200deg, #d9c6b8 0%, #b89a86 50%, #6d5a50 100%); }
  .inside__waves { position: absolute; left: 0; top: 0; width: 660px; height: 500px; pointer-events: none; }
  .inside__copy {
    position: absolute; top: 222px; left: 20px; right: 18px; color: var(--ink-light);
    font-size: 8.5px; line-height: 1.5; font-weight: 600;
  }
  .inside__copy h2 { font-weight: 300; font-size: 17px; margin-bottom: 12px; letter-spacing: .3px; }
  .inside__copy p + p { margin-top: 10px; }
  .inside__copy--no-heading { top: 252px; }
  .inside__footnote {
    position: absolute; left: 20px; bottom: 18px; font-size: 6px; color: rgba(255,255,255,.75);
  }
  .inside__footnote::before {
    content: ""; display: block; width: 120px; border-top: 1px solid rgba(255,255,255,.35); margin-bottom: 4px;
  }
</style>
</head>
<body>

<!-- Outside of the trifold -->
<section class="spread spread--outside" aria-label="Brochure outside">
  <article class="panel panel--cover-back">
    <div class="cover-back__photo" role="img" aria-label="Photo of a commercial truck on the road, tinted blue"></div>
    <h2 class="cover-back__title">Bureau of Freight Haulage Drug Testing</h2>
    <p class="cover-back__text">We offer BFH and Non-BFH drug testing onsite and this can be done on the same day as your BFH exam.</p>
  </article>

  <article class="panel panel--contact">
    <h2 class="contact__heading">VISIT US</h2>
    <p class="contact__address">4120 East Larkspur Road<br>Aldercrest Village, CO 80199</p>
    <div class="contact__map" role="img" aria-label="Street map showing the clinic location near the interstate and Larkspur Road"></div>
    <p class="contact__directions">Our clinic sits on the south side of Larkspur Road, just east of the interstate. Parking is free and the entrance faces the main lot.</p>
    <svg class="contact__wave" viewBox="0 0 220 240" aria-hidden="true">
      <defs>
        <linearGradient id="contactBlue" x1="0" y1="0" x2="1" y2="1">
          <stop offset="0" stop-color="#3b82d2"/>
          <stop offset="1" stop-color="#0455a3"/>
        </linearGradient>
      </defs>
      <path d="M0 40 C70 10 150 0 220 20 L220 240 L0 240 Z" fill="#7fb2ea"/>
      <path d="M0 52 C80 24 150 18 220 36 L220 180 C150 200 70 190 0 200 Z" fill="url(#contactBlue)"/>
      <path d="M0 200 C70 190 150 200 220 180 L220 240 L0 240 Z" fill="#ffffff"/>
    </svg>
    <div class="contact__details">
      <span class="brand-name"><span class="brand-name__dot"></span>Birchwell Family Medicine</span>
      <p class="contact__phone">PHONE: (303) 555-0148<br>FAX: (303) 555-0172</p>
    </div>
    <p class="web-address">www.kellanmoorclinic.com</p>
  </article>

  <article class="panel panel--cover-front">
    <div class="cover-front__brand"><span class="brand-name"><span class="brand-name__dot"></span>Birchwell Family Medicine</span></div>
    <div class="cover-front__photo" role="img" aria-label="Photo of a worker in a hard hat beside a forklift"></div>
    <svg class="cover-front__band" viewBox="0 0 220 300" aria-hidden="true">
      <defs>
        <linearGradient id="frontBlue" x1="0" y1="0" x2="1" y2="1">
          <stop offset="0" stop-color="#5a9be0"/>
          <stop offset="1" stop-color="#0455a3"/>
        </linearGradient>
      </defs>
      <path d="M0 30 C80 0 150 8 220 0 L220 300 L0 300 Z" fill="#a9cdf3"/>
      <path d="M0 42 C80 14 150 20 220 12 L220 230 C150 246 70 238 0 250 Z" fill="url(#frontBlue)"/>
      <path d="M0 250 C70 238 150 246 220 230 L220 300 L0 300 Z" fill="#ffffff"/>
    </svg>
    <ul class="cover-front__services">
      <li>BFH Examination</li>
      <li>BFH Drug Testing</li>
      <li>QWLPA<br>Certified Providers</li>
    </ul>
    <p class="web-address">www.kellanmoorclinic.com</p>
  </article>
</section>

<!-- Inside of the trifold -->
<section class="spread spread--inside" aria-label="Brochure inside">
  <article class="panel">
    <div class="inside__photo inside__photo--eye" role="img" aria-label="Photo of a vision test at an eye examination device"></div>
  </article>
  <article class="panel">
    <div class="inside__photo inside__photo--pressure" role="img" aria-label="Photo of a blood pressure gauge held in a hand"></div>
  </article>
  <article class="panel">
    <div class="inside__photo inside__photo--ear" role="img" aria-label="Photo of an ear being checked with an otoscope"></div>
  </article>

  <svg class="inside__waves" viewBox="0 0 660 500" aria-hidden="true">
    <defs>
      <linearGradient id="insideBlue" x1="0" y1="0" x2="1" y2="1">
        <stop offset="0" stop-color="#1d5fae"/>
        <stop offset=".5" stop-color="#2f73c4"/>
        <stop offset="1" stop-color="#4a8fdb"/>
      </linearGradient>
    </defs>
    <path d="M0 190 C180 150 420 150 660 160 L660 500 L0 500 Z" fill="#8fbdf0"/>
    <path d="M0 204 C180 170 420 168 660 176 L660 500 L0 500 Z" fill="url(#insideBlue)"/>
    <line x1="220" y1="175" x2="220" y2="500" stroke="rgba(0,0,0,.08)"/>
    <line x1="440" y1="168" x2="440" y2="500" stroke="rgba(0,0,0,.08)"/>
  </svg>

  <div class="inside__copy" style="left:20px; width:182px;">
    <h2>ABOUT US</h2>
    <p>Birchwell Family Medicine is a physician owned and operated medical practice in the Larkspur Business Park area of metro Denver, Colorado.</p>
    <p>Our mission is to provide commercial drivers with fast and convenient BFH exams by one of our QWLPA certified providers as well and BFH drug screening.</p>
  </div>

  <div class="inside__copy" style="left:240px; width:182px;">
    <h2>BFH Exam</h2>
    <p>For commercial motor vehicle drivers, the most important safety feature is YOU – the driver! Each time you turn the key, you are responsible for your own safety, as well as the safety of all the people who share the road with you.<br>The physical examination you take for your medical certificate confirms that you are healthy enough to safely perform the demanding job of a commercial motor vehicle driver and keep our Nation’s roads safe. <sup>1</sup></p>
  </div>
  <p class="inside__footnote" style="left:240px;">1 – quote from the FHSA website</p>

  <div class="inside__copy inside__copy--no-heading" style="left:460px; width:182px;">
    <p>Commercial motor vehicle drivers must maintain a current Medical Examiners Certificate to drive. Drivers must have their exam completed by a QWLPA certified provider.</p>
    <p>BFH examinations determine a driver’s physical qualification to operate a commercial motor vehicle. Medical Examiners Certificates must be renewed at least every two years.</p>
  </div>
</section>

</body>
</html>
```